political campaign lawn sign - Governor's Council in Massachuesetts

We are looking for a political lawn sign. We are running a campaign for Governor's Council in Massachusetts. This sign will be on the lawn of homes and businesses so people driving by will see it. It needs to be simple and bold. The last name is long so maybe it could say vote for Marty and then Kolbeck will be big a bold on the next line??
We need it to say:
Vote for Martin Kolbeck
Governor's Council.

Target Market(s)

local residents

Industry/Entity Type

Politcal Campaign

Font styles to use
Sans Serif
Other font styles liked:
• not sure what font but a modern looking one such as Helvetica, Arial, Sans Seri, sharp sans..

Colors
0054AA
0677BA
7BADD7
CADEEF
E8F1F8
00AB8E
00BBA5
67D7C9
C6EFE9
E9F9F6
FFF300
FFF600
FEFA6F
FFFEC7
FFFEE8

Requirements
Must have
• My name written out with a Capital D and R but lower case for every other letter so its Marty Kolbeck
Nice to have
• modern font , the Colors of the lawn sign should have Blue, Yellow and White something bold that will stand out
Should not have
• any maps of Massachusetts

```html
<!DOCTYPE html>
<html lang="en">
<head>
<meta charset="UTF-8">
<title>Vote for Martin Kolbeck – Governor's Council</title>
<link rel="stylesheet" href="https://fonts.googleapis.com/css2?family=Raleway:wght@500;700;800&family=Russo+One&display=swap">
<style>
  :root {
    --page-bg: #070b22;
    --sign-blue: #263b9e;
    --sign-blue-deep: #1f3190;
    --campaign-yellow: #fff300;
    --white: #ffffff;
    --ink: #0b0b0b;
    --rule: rgba(255,255,255,0.75);
  }
  * { margin: 0; padding: 0; box-sizing: border-box; }
  html, body {
    width: 891px; height: 1200px; overflow: hidden;
    background: var(--page-bg);
  }
  .lawn-sign {
    position: absolute;
    left: 30px; top: 462px;
    width: 831px; height: 276px;
    background: linear-gradient(135deg, var(--sign-blue) 0%, var(--sign-blue-deep) 55%, var(--sign-blue) 100%);
    overflow: hidden;
  }
  .megaphone-photo {
    position: absolute;
    left: 0; top: 54px;
    width: 135px; height: 213px;
    background: linear-gradient(160deg, #e6e6e6 0%, #a9a9a9 55%, #3a3a3a 100%);
    border-radius: 0 40px 0 0;
  }
  .vote-block {
    position: absolute;
    left: 146px; top: 61px;
    width: 173px; height: 133px;
    border-top: 1px solid var(--rule);
    border-bottom: 1px solid var(--rule);
    text-align: center;
    color: var(--white);
    font-family: "Russo One", sans-serif;
    text-transform: uppercase;
    line-height: 1;
  }
  .vote-block .vote { display: block; font-size: 60px; margin-top: 14px; letter-spacing: 1px; }
  .vote-block .for  { display: block; font-size: 52px; margin-top: 2px; letter-spacing: 1px; }
  .candidate-first,
  .candidate-last {
    position: absolute;
    left: 359px;
    font-family: "Raleway", sans-serif;
    line-height: 1;
    white-space: nowrap;
  }
  .candidate-first {
    top: 38px;
    font-size: 94px; font-weight: 500;
    color: var(--white);
    letter-spacing: -1px;
  }
  .candidate-last {
    top: 104px;
    font-size: 86px; font-weight: 800;
    color: var(--campaign-yellow);
    letter-spacing: -1px;
  }
  .stars {
    position: absolute;
    left: 684px; top: 76px;
    width: 126px; height: 38px;
  }
  .office-band {
    position: absolute;
    left: 0; top: 0;
    width: 831px; height: 276px;
  }
  .office-title {
    position: absolute;
    left: 395px; top: 233px;
    font-family: "Raleway", sans-serif;
    font-weight: 700;
    font-size: 36px;
    line-height: 1;
    color: var(--ink);
    white-space: nowrap;
  }
</style>
</head>
<body>
  <main class="lawn-sign">
    <div class="megaphone-photo" role="img" aria-label="Black and white photo of a hand holding a megaphone"></div>

    <div class="vote-block">
      <span class="vote">Vote</span>
      <span class="for">For</span>
    </div>

    <div class="candidate-first">Martin</div>
    <div class="candidate-last">Kolbeck</div>

    <svg class="stars" viewBox="0 0 126 38" aria-hidden="true">
      <g fill="var(--campaign-yellow)">
        <polygon points="20,2 24.7,14.5 38,14.5 27.3,22.5 31.3,35.5 20,27.5 8.7,35.5 12.7,22.5 2,14.5 15.3,14.5"/>
        <polygon transform="translate(43 0)" points="20,2 24.7,14.5 38,14.5 27.3,22.5 31.3,35.5 20,27.5 8.7,35.5 12.7,22.5 2,14.5 15.3,14.5"/>
        <polygon transform="translate(86 0)" points="20,2 24.7,14.5 38,14.5 27.3,22.5 31.3,35.5 20,27.5 8.7,35.5 12.7,22.5 2,14.5 15.3,14.5"/>
      </g>
    </svg>

    <svg class="office-band" viewBox="0 0 831 276" aria-hidden="true">
      <polygon fill="var(--campaign-yellow)" points="377,230 831,230 831,276 0,276 0,267 341,267"/>
    </svg>
    <div class="office-title">Governer's Council.</div>
  </main>
</body>
</html>
```